Animal Feed Bag Packaging Design

The task is to design a livestock feed bag. These are 18"x32" and typically hold 50 LBS of feed. This design will be on all of the packaging for our feed bags. These feed bags will be sold in local feed and hardware stores and will hold a variety of different feed products for all classes of livestock. The bags will be double sided. I would like the back side to remain consistent, but I would like the front of the bag to have 4 different varieties that share the same layout, but incorporate different titles and possible graphics. The Categories will be:
- "Poultry Feed" This will be for all classes of poultry
- "Hog Feed" This will be for all classes of hogs
- "Mixed Feed" This will be a sort of catch all design that will be used for a variety of different types of livestock feed (cows, goats, sheep, rabbits)
- "Feed & Grain": This will also be a miscelaneous category that will be used for whole grains and feeds that can be used across multiple animal types.

I have attached many photos that may or may not be used, but that may help to portray our operation and what we do.

Target Market(s)

Backyard Hobby Farmers and Livestock Enthusists

Industry/Entity Type

Agriculture

Font styles to use
Serif

Colors

Designer to choose colors to be used in the design.

Requirements
Must have
• Must contain our logo and have a strong brand presence for "Calloway Kin's Feed". Each bag needs to contain the the following on either the front or backside of the bag. Calloway Kin's Feed - 214 North Willow Lane Brackmoor Utah, 61392 - 608 271 5519 - callowaykinsfeed.example
Nice to have
• Our brand is built around these factors that could be incorporated into the design: Locally Milled, Quality Ingredients, Balanced Nutrition, Family Owned & Operated Est. 2017. Home delivery is also a core competency of our operation. I will attach a few images of our farm where we operate at that may be incorporated if it fits the style.

```html
<!DOCTYPE html>
<html lang="en">
<head>
<meta charset="utf-8">
<title>Calloway Kin's Feed – Feed &amp; Grain Bag Front</title>
<link rel="stylesheet" href="https://fonts.googleapis.com/css2?family=Alfa+Slab+One&family=Fira+Sans:wght@500;600&display=swap">
<style>
  :root {
    --bg: #f2f2f0;
    --bag-white: #ffffff;
    --cream: #ede6d3;
    --red: #9e1418;
    --red-star: #b5241f;
    --ribbon: #2a2a2a;
    --ink: #1b1b1b;
    --olive: #9fb23e;
    --band-text: #f1e6cf;
  }
  * { box-sizing: border-box; margin: 0; padding: 0; }
  html, body {
    width: 1200px; height: 1200px; overflow: hidden;
    background: var(--bg);
  }
  .bag-front {
    position: absolute; left: 210px; top: 20px;
    width: 780px; height: 1160px;
    background: var(--bag-white);
    overflow: hidden;
  }
  .band { position: absolute; left: 0; width: 100%; }
  .band--cream { top: 530px; height: 302px; background: var(--cream); }
  .band--red { top: 832px; height: 140px; background: var(--red); }

  .brand-ribbon {
    position: absolute; left: 44px; top: 0;
    width: 306px; height: 636px;
  }
  .brand-ribbon svg { display: block; width: 100%; height: 100%; }

  .brand-name {
    position: absolute; left: 44px; top: 350px; width: 306px;
    display: flex; flex-direction: column; align-items: center; gap: 14px;
  }
  .brand-name__dot {
    width: 64px; height: 64px; border-radius: 50%;
    background: var(--olive);
  }
  .brand-name__text {
    font-family: "Alfa Slab One", serif;
    color: var(--olive);
    font-size: 20px; letter-spacing: 2px; text-transform: uppercase;
    text-align: center;
  }

  .rating {
    position: absolute; left: 44px; top: 640px; width: 306px;
    text-align: center; color: var(--red-star);
    font-size: 20px; letter-spacing: 1px; line-height: 1;
  }
  .product-title {
    position: absolute; left: 44px; top: 672px; width: 306px;
    font-family: "Alfa Slab One", serif;
    font-size: 60px; line-height: 1.0; color: var(--ink);
    text-align: center; letter-spacing: 1px;
  }

  .rooster-art {
    position: absolute; left: 372px; top: 320px;
    width: 400px; height: 468px;
    background: radial-gradient(ellipse at 55% 45%, #7d7d7a 0%, #b5b3ac 55%, rgba(237,230,211,0) 78%);
  }
  .sack-art {
    position: absolute; left: 76px; top: 872px;
    width: 248px; height: 260px;
    background: linear-gradient(180deg, #7e1214 0%, #7e1214 30%, #3a3a3a 55%, #9a9a9a 100%);
    border-radius: 40px 40px 20px 20px;
  }

  .benefits {
    position: absolute; left: 390px; top: 852px; width: 340px;
    list-style: none; text-align: center;
    font-family: "Alfa Slab One", serif;
    font-variant: small-caps;
    font-size: 23px; line-height: 29px;
    color: var(--band-text); letter-spacing: 0.5px;
  }

  .contact {
    position: absolute; left: 380px; top: 1008px; width: 370px;
    font-family: "Fira Sans", sans-serif; font-weight: 600;
    font-size: 15px; line-height: 26px; color: var(--ink);
    text-align: center; font-style: normal;
  }
</style>
</head>
<body>
  <main class="bag-front">
    <div class="band band--cream"></div>
    <div class="band band--red"></div>

    <div class="brand-ribbon">
      <svg viewBox="0 0 306 636" preserveAspectRatio="none" aria-hidden="true">
        <polygon points="0,0 306,0 306,636 153,592 0,636" fill="#2a2a2a"/>
      </svg>
    </div>

    <div class="brand-name">
      <span class="brand-name__dot"></span>
      <span class="brand-name__text">Calloway Kin's Feed</span>
    </div>

    <div class="rating" aria-label="Five stars">★★★★★</div>
    <h1 class="product-title">FEED &amp;<br>GRAIN</h1>

    <div class="rooster-art" role="img" aria-label="Engraved illustration of a rooster standing in tall grass"></div>
    <div class="sack-art" role="img" aria-label="Engraved illustration of an open burlap sack full of grain"></div>

    <ul class="benefits">
      <li>• Locally Milled •</li>
      <li>• Quality Ingredients •</li>
      <li>• Balanced Nutrition •</li>
    </ul>

    <address class="contact">
      Calloway Kin's Feed,<br>
      214 North Willow Lane Brackmoor Utah, 61392<br>
      Tel: 608 271 5519 • www.callowaykinsfeed.example
    </address>
  </main>
</body>
</html>
```